RW dental business card. A family dental practice.

Logo plus the following details.

RW Dental
Dr. Marcus Ellory D.D.S
Family. Implant.Cosmetic

48 Fernbrook Lane, Unit 12-13
Markham, ON K2P7R4

Tel: 905-318-2670
Fx:905-318-9025
rwdental-sample.ca

On the double side:

Next app: ______________________

Please notify us at least 48hours in advance to avoid cancellation fees.

Target Market(s)

Family Dental Services

Industry/Entity Type

Dental

Contact Information for Business Card

Put logo prominently and all the info along with it.

Font styles to use
Other font styles liked:
• See Logo Font

Colors
0255a3
3277b5
85acd3
00a990
33b8a4

Requirements
Must have
• Logo and the info stated above.
• See the logo color scheme.
• Or a grayscale (Black, white gray) combination
Nice to have
• A modern unique layout
Should not have
• too simple a design

```html
<!DOCTYPE html>
<html lang="en">
<head>
<meta charset="utf-8">
<title>RW Dental – Business and Appointment Cards</title>
<link rel="stylesheet" href="https://fonts.googleapis.com/css2?family=Alegreya+Sans:wght@400;500&family=Source+Sans+3:ital,wght@0,400;0,600;1,400&display=swap">
<style>
  :root {
    --navy: #1b3452;
    --navy-text: #1c3b6c;
    --teal: #3ec8c0;
    --white: #ffffff;
    --page: #ebe8e3;
    --grey-text: #5a5a5a;
    --soft-grey: #e4e5e9;
    --soft-teal: #e3f5f4;
  }
  * { margin: 0; padding: 0; box-sizing: border-box; }
  html, body { width: 1200px; height: 987px; overflow: hidden; }
  body { background: var(--page); position: relative; font-family: "Source Sans 3", sans-serif; }

  .card { position: absolute; background: var(--white); overflow: hidden; box-shadow: 0 2px 6px rgba(0,0,0,.18); }

  /* Front business card */
  .card-front { left: 318px; top: 164px; width: 540px; height: 308px; font-family: "Alegreya Sans", sans-serif; }
  .front-art { position: absolute; left: 0; top: 0; width: 300px; height: 308px;
    background: radial-gradient(ellipse at 45% 45%, var(--soft-teal) 0%, var(--soft-grey) 45%, var(--white) 80%); }
  .front-shape { position: absolute; inset: 0; }
  .front-details { position: absolute; right: 26px; top: 0; text-align: right; color: var(--white); }
  .doctor-name { position: absolute; right: 0; top: 64px; white-space: nowrap; color: var(--teal); font-size: 19px; font-weight: 500; }
  .doctor-name small { font-size: 12px; }
  .specialties { position: absolute; right: 0; top: 88px; white-space: nowrap; font-size: 14px; }
  .address { position: absolute; right: 0; top: 117px; white-space: nowrap; font-size: 14px; line-height: 19px; }
  .contact { position: absolute; right: 0; top: 185px; white-space: nowrap; font-size: 14px; line-height: 20px; }
  .contact li { list-style: none; display: flex; justify-content: flex-end; align-items: center; gap: 8px; }
  .contact svg { width: 13px; height: 13px; fill: var(--teal); }

  /* Appointment cards */
  .card-appt { top: 504px; width: 538px; height: 307px; color: var(--navy-text); }
  .card-appt.left { left: 54px; }
  .card-appt.right { left: 608px; }
  .appt-title { position: absolute; left: 25px; top: 33px; font-size: 21px; font-weight: 600; }
  .brand { position: absolute; color: var(--navy-text); }
  .left .brand { left: 262px; top: 26px; }
  .right .brand { left: 0; right: 0; top: 24px; text-align: center; }
  .brand-name { font-size: 26px; font-weight: 400; line-height: 1.1; }
  .right .brand-name { font-size: 30px; }
  .brand-tag { font-size: 12px; margin-top: 3px; }
  .right .brand-tag { font-size: 14px; }

  .row { position: absolute; left: 25px; right: 25px; display: flex; align-items: baseline; font-size: 15px; }
  .fill { flex: 1; border-bottom: 1.5px dotted #444; margin: 0 4px; transform: translateY(-4px); }
  .row-name { top: 108px; }
  .row-name .label { color: var(--grey-text); }
  .row-date { top: 163px; }
  .row-date .fill.date { flex: 2.1; margin-right: 8px; }
  .ampm { font-size: 12px; }
  .days { position: absolute; left: 30px; right: 30px; top: 216px; display: flex; justify-content: space-between; font-size: 14px; }
  .days span { display: flex; align-items: center; gap: 6px; }
  .days span::after { content: ""; width: 14px; height: 12px; border: 1.3px solid var(--navy-text); }
  .notice { position: absolute; left: 0; right: 0; top: 260px; text-align: center; font-style: italic; font-size: 11.5px; line-height: 15px; color: var(--grey-text); }
</style>
</head>
<body>

<section class="card card-front">
  <div class="front-art" role="img" aria-label="Soft faded background artwork"></div>
  <svg class="front-shape" viewBox="0 0 540 308" aria-hidden="true">
    <path d="M298 0 C300 130 240 240 116 308 L206 308 C280 230 310 120 307 0 Z" fill="var(--teal)"/>
    <path d="M307 0 L540 0 L540 308 L206 308 C280 230 310 120 307 0 Z" fill="var(--navy)"/>
    <path d="M307 0 C310 120 280 230 206 308" fill="none" stroke="var(--white)" stroke-width="3"/>
  </svg>
  <div class="front-details">
    <p class="doctor-name">Dr. Marcus Ellory <small>D.D.S</small></p>
    <p class="specialties">Family. Implant. Cosmetic</p>
    <p class="address">48 Fernbrook Lane<br>Unit 12-13<br>Markham, ON K2P7R4</p>
    <ul class="contact">
      <li>905-318-2670 <svg viewBox="0 0 24 24"><path d="M6.6 10.8a15 15 0 0 0 6.6 6.6l2.2-2.2c.3-.3.7-.4 1-.2 1.1.4 2.3.6 3.6.6.6 0 1 .4 1 1V20c0 .6-.4 1-1 1A17 17 0 0 1 3 4c0-.6.4-1 1-1h3.5c.6 0 1 .4 1 1 0 1.3.2 2.5.6 3.6.1.3 0 .7-.2 1z"/></svg></li>
      <li>905-318-9025 <svg viewBox="0 0 24 24"><path d="M6 2h10l2 2v5H6zM3 10h18a1 1 0 0 1 1 1v7H2v-7a1 1 0 0 1 1-1zm3 10h12v2H6z"/></svg></li>
      <li>www.rwdental-sample.ca <svg viewBox="0 0 24 24"><path d="M12 2a10 10 0 1 0 0 20 10 10 0 0 0 0-20zm-1 17.9A8 8 0 0 1 4.2 10l4.8 4.8v1a2 2 0 0 0 2 2zm6.9-2.5A2 2 0 0 0 16 16h-1v-3a1 1 0 0 0-1-1H8v-2h2a1 1 0 0 0 1-1V7h2a2 2 0 0 0 2-2v-.4a8 8 0 0 1 2.9 12.8z"/></svg></li>
    </ul>
  </div>
</section>

<section class="card card-appt left">
  <h2 class="appt-title">Next Appointment</h2>
  <div class="brand">
    <p class="brand-name">RW Dental</p>
    <p class="brand-tag">Your dental health support Team</p>
  </div>
  <div class="row row-name"><span class="fill"></span><span class="label">has an apppointment</span></div>
  <div class="row row-date">Date :<span class="fill date"></span>Time :<span class="fill"></span><span class="ampm">AM/PM</span></div>
  <div class="days"><span>Sun</span><span>Mon</span><span>Tue</span><span>Wed</span><span>Thu</span><span>Fri</span><span>Sat</span></div>
  <p class="notice">Please give me 48 hours notice if you are unable to keep your appointment or<br>a cancellation fee may be charged.</p>
</section>

<section class="card card-appt right">
  <div class="brand">
    <p class="brand-name">RW Dental</p>
    <p class="brand-tag">Your dental health support Team</p>
  </div>
  <div class="row row-name"><span class="fill"></span><span class="label">has an apppointment</span></div>
  <div class="row row-date">Date :<span class="fill date"></span>Time :<span class="fill"></span><span class="ampm">AM/PM</span></div>
  <div class="days"><span>Sun</span><span>Mon</span><span>Tue</span><span>Wed</span><span>Thu</span><span>Fri</span><span>Sat</span></div>
  <p class="notice">Please give me 48 hours notice if you are unable to keep your appointment or<br>a cancellation fee may be charged.</p>
</section>

</body>
</html>
```